Flyer Design

We are a property company and need attractive flyers that will grab peoples attention. We want them to be bold but simple and not too busy. I attach a draft and also our logo. We will print in A5 size.
Thank you & I look forward to receiving designs.

It Company

```html
<!DOCTYPE html>
<html lang="en">
<head>
<meta charset="utf-8">
<title>Orla Developments – Subdivision Flyer</title>
<link rel="stylesheet" href="https://fonts.googleapis.com/css2?family=Cinzel:wght@400;700&display=swap">
<style>
  :root {
    --backdrop: #2f2f2f;
    --paper: #efece6;
    --paper-edge: #e2ddd3;
    --wood-light: #ddd3c3;
    --wood-mid: #cfc3ae;
    --gold: #a27b2c;
    --gold-dark: #7c5b1d;
    --brand-brown: #6e4c2c;
    --blue: #1b66b1;
    --ink: #2b2926;
    --white: #ffffff;
  }
  * { margin: 0; padding: 0; box-sizing: border-box; }
  html, body {
    width: 1125px; height: 1200px; overflow: hidden;
    background: var(--backdrop);
  }
  .flyer {
    position: absolute; left: 162px; top: 30px;
    width: 800px; height: 1140px; overflow: hidden;
    background: linear-gradient(180deg, var(--paper) 0%, var(--paper-edge) 100%);
    font-family: "Cinzel", "Times New Roman", serif;
    text-align: center;
    color: var(--ink);
  }
  .header-band, .footer-band { position: absolute; left: 0; width: 800px; }
  .header-band { top: 0; height: 320px; }
  .footer-band { bottom: 0; height: 150px; }

  .brand {
    position: absolute; top: 150px; left: 0; width: 100%;
    display: flex; justify-content: center; align-items: center; gap: 14px;
    font-size: 39px; font-weight: 400; letter-spacing: 1px;
    color: var(--brand-brown);
  }
  .brand-mark { width: 16px; height: 16px; background: var(--brand-brown); }

  .block { position: absolute; left: 0; width: 100%; }
  .headline {
    top: 345px; color: var(--blue);
    font-size: 31px; font-weight: 700; line-height: 53px; letter-spacing: 0.5px;
  }
  .question {
    top: 565px; font-size: 37px; font-weight: 400; line-height: 56px;
  }
  .intro {
    top: 710px; font-size: 23px; line-height: 40px;
  }
  .contact {
    top: 795px; color: var(--blue); font-weight: 700;
  }
  .contact-call { font-size: 37px; line-height: 54px; }
  .contact-email { font-size: 29px; line-height: 46px; }
  .contact .or { color: var(--gold); }
  .icon { display: inline-block; vertical-align: middle; }
  .info {
    top: 902px; font-size: 23px; line-height: 39px;
  }
  .website {
    position: absolute; top: 1092px; left: 0; width: 100%;
    font-size: 22px; line-height: 30px; color: var(--ink);
    display: flex; justify-content: center; align-items: center; gap: 10px;
  }
</style>
</head>
<body>
  <main class="flyer">
    <svg class="header-band" viewBox="0 0 800 320" role="img" aria-label="Light oak wood grain texture behind the company name">
      <defs>
        <linearGradient id="wood" x1="0" y1="0" x2="1" y2="0">
          <stop offset="0" stop-color="var(--wood-mid)"/>
          <stop offset="0.5" stop-color="var(--wood-light)"/>
          <stop offset="1" stop-color="var(--wood-mid)"/>
        </linearGradient>
      </defs>
      <rect width="800" height="320" fill="url(#wood)"/>
      <path d="M0 205 Q 400 395 800 162 L800 320 L0 320 Z" fill="var(--paper)"/>
      <path d="M0 172 Q 380 362 800 128" fill="none" stroke="var(--gold)" stroke-width="14"/>
      <path d="M0 190 Q 385 380 800 146" fill="none" stroke="var(--white)" stroke-width="7"/>
      <path d="M0 204 Q 400 392 800 162" fill="none" stroke="var(--gold-dark)" stroke-width="9"/>
    </svg>

    <div class="brand"><span class="brand-mark"></span>Orla Developments</div>

    <div class="block headline">
      Are you a homeowner<br>
      looking for financial freedom<br>
      while been able to<br>
      keep your own home?
    </div>

    <div class="block question">
      Are you struggling to pay<br>
      your mortgage?
    </div>

    <div class="block intro">
      Orla specialise in subdivisions including<br>
      finance and management.
    </div>

    <div class="block contact">
      <div class="contact-call">
        Call
        <svg class="icon" width="30" height="30" viewBox="0 0 30 30" aria-hidden="true">
          <circle cx="15" cy="15" r="13" fill="none" stroke="var(--gold)" stroke-width="2"/>
          <path d="M10.5 8.5 l3 3 -1.6 1.8 c1 2 2.5 3.5 4.5 4.5 l1.8 -1.6 3 3 -1.8 2 c-5 -0.5 -10 -5.5 -10.6 -10.6 z" fill="var(--gold)"/>
        </svg>
        021 555 014 <span class="or">or</span>
      </div>
      <div class="contact-email">
        email
        <svg class="icon" width="30" height="22" viewBox="0 0 30 22" aria-hidden="true">
          <rect x="2" y="2" width="26" height="18" fill="none" stroke="var(--gold)" stroke-width="2"/>
          <path d="M2 2 L15 13 L28 2 M2 20 L11 10 M28 20 L19 10" fill="none" stroke="var(--gold)" stroke-width="2"/>
        </svg>
        info@orlasubdivisions.com
      </div>
    </div>

    <div class="block info">
      for more information or to find out<br>
      if your property is suitable<br>
      for subdivision in Auckland.
    </div>

    <svg class="footer-band" viewBox="0 0 800 150" aria-hidden="true">
      <path d="M0 60 Q 300 -5 800 85 L800 150 L0 150 Z" fill="var(--paper)"/>
      <path d="M0 52 Q 300 -12 800 78" fill="none" stroke="var(--gold)" stroke-width="14"/>
      <path d="M0 68 Q 300 4 800 92" fill="none" stroke="var(--white)" stroke-width="6"/>
      <path d="M0 80 Q 320 18 800 104" fill="none" stroke="var(--gold-dark)" stroke-width="8"/>
    </svg>

    <div class="website">
      <svg class="icon" width="20" height="20" viewBox="0 0 20 20" aria-hidden="true">
        <circle cx="10" cy="10" r="8.5" fill="none" stroke="var(--gold)" stroke-width="1.6"/>
        <ellipse cx="10" cy="10" rx="3.6" ry="8.5" fill="none" stroke="var(--gold)" stroke-width="1.4"/>
        <path d="M1.5 10 H18.5 M3 5.5 H17 M3 14.5 H17" stroke="var(--gold)" stroke-width="1.2"/>
      </svg>
      www.orlasubdivisions.com
    </div>
  </main>
</body>
</html>
```